Commercial real estate Brokerage logo, letterhead and business card design

Boutique Commercial real Estate Brokerage and development company requires logo, letterhead/stationary and business card design. For reference, competitors include Harper Vale Brightwood, Pemberton & Oakhurst, Renwick Galloway and Tamsin which all have designs which evoke strong corporate image.
Updates

The name of the firm is Brantley Real Estate. If you look at my competitors web sites you will see their logos. I am looking for something that has a similar flavor - not the same colors or graphics - just how you feel when you see their logo. 
1. www.hvb-realty.example
2. http://www.tamsinprop.example/en-us
3. http://www.pembertonoakhurst.example/

Industry/Entity Type

Real Estate

```html
<!DOCTYPE html>
<html lang="en">
<head>
<meta charset="utf-8">
<title>Brantley Real Estate — Stationery</title>
<link rel="stylesheet" href="https://fonts.googleapis.com/css2?family=Cinzel:wght@600;700&family=Open+Sans:wght@400;600&display=swap">
<style>
  :root {
    --backdrop: #6e4a2c;
    --paper: #ffffff;
    --paper-shade: #ececec;
    --ink: #1a1a1a;
    --ink-soft: #444444;
    --band-dark: #141414;
    --band-grey: #7d7d7d;
    --rule: #555555;
    --label: #111111;
  }
  * { box-sizing: border-box; margin: 0; padding: 0; }
  html, body { width: 1200px; height: 535px; overflow: hidden; }
  body {
    position: relative;
    background: var(--backdrop);
    font-family: "Open Sans", Arial, sans-serif;
    color: var(--ink);
  }
  .sheet {
    position: absolute;
    background: linear-gradient(135deg, var(--paper) 40%, var(--paper-shade));
    box-shadow: 0 2px 6px rgba(0,0,0,.35);
    overflow: hidden;
  }
  .wordmark {
    position: absolute;
    font-family: "Cinzel", "Times New Roman", serif;
    font-weight: 700;
    line-height: 1.05;
    letter-spacing: .06em;
    color: var(--ink);
    text-align: center;
  }
  .foot-band { position: absolute; left: 0; bottom: 0; width: 100%; height: 6px; }
  .tiny { font-size: 5.5px; line-height: 1.6; color: var(--ink-soft); }

  /* Letterhead */
  .letterhead { top: 34px; width: 336px; height: 434px; }
  .letterhead--one { left: 32px; }
  .letterhead--two { left: 406px; }
  .letterhead .wordmark { left: 18px; top: 18px; font-size: 15px; }
  .contact-block {
    position: absolute; left: 256px; top: 16px;
    border-left: 1px solid var(--rule); padding-left: 4px;
  }
  .contact-block span::before { content: "● "; font-size: 4px; vertical-align: middle; }
  .address-block {
    position: absolute; left: 264px; top: 20px;
    border-left: 1px solid var(--rule); padding-left: 4px; font-size: 5.5px; line-height: 1.5; color: var(--ink-soft);
  }
  .letterhead-address {
    position: absolute; left: 104px; bottom: 9px;
    font-size: 6.5px; letter-spacing: .04em; color: var(--ink-soft);
  }

  /* Fax */
  .fax-title { position: absolute; left: 17px; top: 96px; font-size: 20px; font-weight: 400; }
  .fax-field {
    position: absolute; height: 10px; border-bottom: 1px solid var(--rule);
    font-size: 5.5px; color: var(--ink-soft);
  }
  .fax-field--left { left: 16px; width: 155px; }
  .fax-field--right { left: 186px; width: 118px; }
  .fax-checks { position: absolute; left: 16px; top: 214px; display: flex; gap: 14px; font-size: 5.5px; color: var(--ink-soft); }
  .fax-checks span { display: flex; align-items: center; gap: 3px; }
  .fax-checks span::before { content: ""; width: 6px; height: 6px; border: 1px solid var(--rule); }
  .fax-footer {
    position: absolute; left: 0; width: 100%; bottom: 10px; text-align: center;
    font-size: 5.5px; color: var(--ink-soft); word-spacing: 2px;
  }

  /* Envelopes */
  .envelope { width: 376px; height: 168px; }
  .envelope--back { left: 794px; top: 36px; background: var(--paper); }
  .envelope--middle { left: 782px; top: 110px; background: linear-gradient(135deg, #fff, #ededed); }
  .envelope--front { left: 758px; top: 194px; width: 374px; }
  .envelope .wordmark { left: 10px; top: 12px; font-size: 15px; text-align: left; }
  .envelope-address { position: absolute; left: 8px; top: 140px; font-size: 6.5px; color: var(--ink-soft); }
  .envelope-url { position: absolute; left: 8px; top: 153px; font-size: 5.5px; letter-spacing: .06em; color: var(--ink-soft); }

  /* Business cards */
  .card { top: 390px; width: 137px; height: 80px; }
  .card--front { left: 778px; }
  .card--back { left: 926px; }
  .card--front .wordmark { left: 12px; top: 27px; font-size: 8.5px; }
  .card-details {
    position: absolute; left: 78px; top: 14px; height: 52px;
    border-left: 1px solid var(--rule); padding-left: 4px; font-size: 3.6px; line-height: 1.5; color: var(--ink-soft);
  }
  .card-name { font-size: 5px; font-weight: 600; color: var(--ink); }
  .card--back .wordmark { left: 0; width: 100%; top: 25px; font-size: 9px; }
  .card-url { position: absolute; left: 0; width: 100%; top: 47px; text-align: center; font-size: 5px; letter-spacing: .06em; color: var(--ink-soft); }

  .option-label { position: absolute; font-size: 24px; color: var(--label); }
</style>
</head>
<body>

  <!-- Letterhead, option one -->
  <section class="sheet letterhead letterhead--one">
    <div class="wordmark">Brantley<br>Real Estate</div>
    <div class="contact-block tiny">
      <span>123-456-7890</span><br>
      <span>123-456-7890</span><br>
      <span>info@brantleyre.example</span><br>
      <span>www.brantleyre.example</span>
    </div>
    <p class="letterhead-address">Street Name, City Name State Zipcode</p>
    <svg class="foot-band" viewBox="0 0 336 6" preserveAspectRatio="none">
      <rect width="336" height="6" fill="var(--band-grey)"/>
      <polygon points="0,0 160,0 166,6 0,6" fill="var(--band-dark)"/>
    </svg>
  </section>

  <!-- Letterhead, option two (fax) -->
  <section class="sheet letterhead letterhead--two">
    <div class="wordmark">Brantley<br>Real Estate</div>
    <div class="address-block">Street Name, City Name<br>State Zipcode</div>
    <h1 class="fax-title">FAX</h1>
    <div class="fax-field fax-field--left" style="top:130px">To :</div>
    <div class="fax-field fax-field--right" style="top:130px">From :</div>
    <div class="fax-field fax-field--left" style="top:148px">Fax :</div>
    <div class="fax-field fax-field--right" style="top:148px">Pages :</div>
    <div class="fax-field fax-field--left" style="top:166px">Phone :</div>
    <div class="fax-field fax-field--right" style="top:166px">Date :</div>
    <div class="fax-field fax-field--left" style="top:184px">Re :</div>
    <div class="fax-field fax-field--right" style="top:184px">CC :</div>
    <div class="fax-checks">
      <span>Urgent</span><span>For Review</span><span>Please Comment</span><span>Please Reply</span><span>Please Recycle</span>
    </div>
    <p class="fax-footer">✆ 123-456-7890 &nbsp;✆ 123-456-7890 &nbsp;✉ info@brantleyre.example &nbsp;● www.brantleyre.example</p>
    <svg class="foot-band" viewBox="0 0 335 6" preserveAspectRatio="none">
      <rect width="335" height="6" fill="var(--band-grey)"/>
      <polygon points="0,0 124,0 130,6 0,6" fill="var(--band-dark)"/>
    </svg>
  </section>

  <!-- Envelopes -->
  <div class="sheet envelope envelope--back">
    <svg width="376" height="168" viewBox="0 0 376 168">
      <polyline points="4,0 180,66 196,66 372,0" fill="none" stroke="#bdbdbd" stroke-width=".8"/>
    </svg>
  </div>
  <div class="sheet envelope envelope--middle">
    <svg width="376" height="168" viewBox="0 0 376 168">
      <path d="M0,0 H376 L366,22 Q360,30 340,36 L240,66 Q188,74 136,66 L36,36 Q16,30 10,22 Z" fill="var(--band-dark)"/>
    </svg>
  </div>
  <section class="sheet envelope envelope--front">
    <div class="wordmark">Brantley<br>Real Estate</div>
    <p class="envelope-address">Street Name, City Name State Zipcode</p>
    <p class="envelope-url">www.brantleyre.example</p>
  </section>

  <!-- Business cards -->
  <section class="sheet card card--front">
    <div class="wordmark">Brantley<br>Real Estate</div>
    <div class="card-details">
      <div class="card-name">Your Name</div>
      Title<br><br>
      ✆ 123-456-7890<br>
      ✆ 123-456-7890<br>
      ✉ info@brantleyre.example<br>
      ● www.brantleyre.example<br><br>
      Street Name, City Name<br>State Zipcode
    </div>
    <svg class="foot-band" style="height:4px" viewBox="0 0 137 4" preserveAspectRatio="none">
      <rect width="137" height="4" fill="var(--band-grey)"/>
      <polygon points="0,0 60,0 63,4 0,4" fill="var(--band-dark)"/>
    </svg>
  </section>
  <section class="sheet card card--back">
    <div class="wordmark">Brantley<br>Real Estate</div>
    <p class="card-url">www.brantleyre.example</p>
    <svg class="foot-band" style="height:4px" viewBox="0 0 137 4" preserveAspectRatio="none">
      <rect width="137" height="4" fill="var(--band-dark)"/>
    </svg>
  </section>

  <p class="option-label" style="left:132px; top:478px">Option-1</p>
  <p class="option-label" style="left:510px; top:470px">Option-2</p>

</body>
</html>
```